Webdesign für eine Softwarewarentwicklung und Consulting für das Gesundheitswesen
Zielgruppe
Softwarewarentwicklung und Consulting für das Gesundheitswesen. Unsere Zielgruppe sind Unternehmen und Organisationen im Bereich des Gesundheitswesen. Weiter informationen auf derzeitiger Homepage unter www.vmt-pflegeloesung.de.
Aufgabenstellung
Das Webdesign sollte deutlich moderner und kreativer wirken als unsere derzeitige Hompage. (Die bisherige Hompage wurde seinerzeit bei der Gründung 'auf die Schnelle' entwickelt.) Die neue Homapage sollte 'frisch' wirken und einem modernen Softwareunternehmen entsprechen.: Schlicht, modern und innovativ. Die Website sollte auch später gut auf Handy und Tablet darstellbar sein. Da wir derzeit wenig Inhalte auf unserer Homepage haben, wären wir auch für inhaltliche Vorschläge dankbar. Unsere Logofarben sollten sich auch im Design wiederfinden (der Rotton hat den Wert RGB: 227, 7, 19 #e30713 - der Blauton hat den Wert RGB: 30, 38, 74 1 #e264a).
Im Format bin ich unerfahren und würde dann für das spätere Umsetzen Adobe Photoshop vorschlagen.
Idealerweise sollte sich das Design später in einem gängigen CMS umsetzen lassen.
Gerne können Sie uns auch ein Komplettangebot auch zum Thema Umsetzung unterbreiten.
Grundsätzlich finde ich folgende Hompages ganz gut:
https://brelvuno.com/
https://www.kiesfeld.de/
https://www.plumvantic.com/de/
https://zirkanu.de/

```html
<!DOCTYPE html>
<html lang="de">
<head>
<meta charset="utf-8">
<title>VMT – Softwareentwicklung für das Gesundheitswesen</title>
<link href="https://fonts.googleapis.com/css2?family=Cabin:wght@400;500;600&family=Nunito+Sans:wght@400;600;700&display=swap" rel="stylesheet">
<style>
:root{
  --navy:#1e264a;
  --navy-2:#243163;
  --blue:#0b5aa0;
  --red:#e30713;
  --orange:#f07a45;
  --grey:#f0f0f0;
  --text:#1e264a;
  --muted:#3b4160;
  --white:#ffffff;
}
*{margin:0;padding:0;box-sizing:border-box}
html,body{width:1200px;height:4408px;overflow:hidden}
body{position:relative;background:var(--white);font-family:"Nunito Sans",sans-serif;color:var(--text)}
.abs{position:absolute}
h1,h2,h3,.brand{font-family:"Cabin",sans-serif;font-weight:500}
.accent{color:var(--red)}
.eyebrow{font-size:10px;letter-spacing:1.5px;text-transform:uppercase;color:var(--red);font-weight:600}
.btn{display:inline-flex;align-items:center;justify-content:center;height:38px;padding:0 20px;border-radius:19px;background:var(--orange);color:var(--white);font-size:13px;font-weight:600;text-decoration:none}
.link{font-size:11px;color:var(--text);text-decoration:none;border-bottom:2px solid var(--orange);padding-bottom:3px}

/* hero */
.hero{left:0;top:0;width:1200px;height:562px;background:
  radial-gradient(ellipse 520px 380px at 1150px 560px, rgba(227,7,19,.95), rgba(227,7,19,0) 70%),
  radial-gradient(ellipse 700px 300px at 700px 300px, rgba(46,90,170,.55), rgba(46,90,170,0) 70%),
  linear-gradient(110deg,#1e264a 0%,#213066 50%,#3a3a7a 80%,#a21a3a 100%)}
.hero-strip{left:0;top:562px;width:88px;height:74px;background:var(--navy)}
.brand{font-size:34px;font-weight:600;color:var(--white);letter-spacing:1px;line-height:1}
.brand-sub{font-size:6px;color:var(--white);letter-spacing:.5px;font-weight:700;margin-top:3px}
.nav{left:262px;top:36px;display:flex;gap:18px;font-size:13px;color:var(--white)}
.nav a{color:var(--white);text-decoration:none;padding-bottom:5px}
.nav a.active{border-bottom:2px solid var(--orange)}
.hero-phone{left:795px;top:34px;display:flex;align-items:center;gap:8px;color:var(--white);font-size:13px}
.btn-outline{left:970px;top:24px;height:38px;width:152px;border:2px solid var(--orange);border-radius:19px;color:var(--white);font-size:13px;display:flex;align-items:center;justify-content:center}
.hero h1{left:176px;top:214px;width:560px;font-size:29px;line-height:1.25;color:var(--white)}
.hero-text{left:176px;top:302px;width:460px;font-size:13.5px;line-height:1.4;color:var(--white)}
.hero .btn{left:176px;top:383px}
.device{left:862px;top:162px;width:338px;height:295px;border-radius:10px 0 0 0;background:linear-gradient(160deg,#2a2f45,#0f1220)}

/* portfolio */
.portfolio-bg{left:0;top:1280px;width:1200px;height:300px;background:var(--grey)}
.portfolio-panel{left:88px;top:562px;width:1112px;height:718px;background:var(--white)}
.sec-head{left:226px}
.portfolio h2{font-size:24px;color:var(--text)}
.portfolio-text{left:226px;top:678px;width:500px;font-size:10.5px;line-height:1.5;color:var(--muted)}
.card{width:276px;height:375px;background:linear-gradient(180deg,#1c3f7c 30%,#0b5aa0 100%);color:var(--white)}
.card .photo{width:276px;height:188px;background:linear-gradient(135deg,#c9c4bd,#7d8591)}
.card h3{font-size:20px;margin:14px 10px 8px;color:var(--white)}
.card p{margin:0 12px;font-size:10px;line-height:1.55}
.card .link{position:absolute;left:10px;bottom:30px;color:var(--white);font-size:10px}

/* features */
.features h2{font-size:24px;line-height:1.22;width:760px}
.feature{width:230px}
.feature h3{font-size:16px;line-height:1.3;margin:16px 0 10px;color:var(--text)}
.feature p{font-size:10px;line-height:1.6;color:var(--muted)}

/* cta */
.cta{left:0;top:2205px;width:1200px;height:438px;background:
  radial-gradient(ellipse 600px 200px at 350px 230px, rgba(60,100,190,.45), rgba(60,100,190,0) 70%),
  var(--navy);color:var(--white);text-align:center}
.cta h2{position:absolute;left:300px;top:124px;width:600px;font-size:24px;line-height:1.25}
.cta p{position:absolute;left:400px;top:200px;width:400px;font-size:11px;line-height:1.5}
.cta .btn{position:absolute;left:524px;top:265px;width:154px}

/* about & jobs */
.lower-bg{left:0;top:2643px;width:1200px;height:1449px;background:var(--grey)}
.panel{background:var(--white)}
.photo-block{background:linear-gradient(150deg,#dfe3e6,#8b96a0)}
.text-block h2{font-size:24px;line-height:1.22}
.text-block p{font-size:10.5px;line-height:1.6;color:var(--muted);margin:22px 0 34px}

/* partners */
.partners{left:0;top:3855px;width:1200px;text-align:center}
.partners h2{font-size:24px;margin-top:10px}
.partner{top:3955px;width:96px;height:32px;border-radius:16px;background:#cfcfd3}

/* footer */
.footer{left:0;top:4092px;width:1200px;height:316px;background:var(--navy);color:var(--white)}
.footer h4{font-family:"Cabin",sans-serif;font-weight:600;font-size:15px;margin-bottom:16px}
.f-col{position:absolute;top:54px;font-size:10.5px}
.f-row{display:flex;gap:10px;align-items:flex-start;margin-bottom:15px;line-height:1.6}
.f-list{list-style:none}
.f-list li{margin-bottom:11px;display:flex;align-items:center;gap:10px}
.f-list li::before{content:"";width:5px;height:5px;background:var(--orange)}
.f-bottom{position:absolute;left:88px;top:282px;width:1024px;display:flex;font-size:9.5px}
.f-bottom .legal{margin-left:128px;display:flex;gap:20px}
</style>
</head>
<body>

<!-- Hero -->
<header class="hero abs">
  <div class="abs" style="left:88px;top:26px">
    <div class="brand">VMT</div>
    <div class="brand-sub">SOFTWARE FÜR DAS GESUNDHEITSWESEN</div>
  </div>
  <nav class="nav abs">
    <a class="active" href="#">Home</a><a href="#">Produkte</a><a href="#">Über Uns</a><a href="#">Jobangebote</a>
  </nav>
  <div class="hero-phone abs">
    <svg width="14" height="14" viewBox="0 0 24 24" fill="#fff"><path d="M6.6 10.8a15.1 15.1 0 006.6 6.6l2.2-2.2a1 1 0 011-.25 11.4 11.4 0 003.6.57 1 1 0 011 1V20a1 1 0 01-1 1A17 17 0 013 4a1 1 0 011-1h3.5a1 1 0 011 1c0 1.25.2 2.45.57 3.57a1 1 0 01-.25 1z"/></svg>
    +49 21 40 / 5 20 18 - 00
  </div>
  <div class="btn-outline abs">Beratung vereinbaren</div>
  <h1 class="abs">Wir entwickeln digitale Anwendungen für die Zukunft im Gesundheitswesen</h1>
  <p class="hero-text abs">Lorem ipsum dolor sit amet, consetetur sadipscing elitr, sed diam nonumy eirmod tempor invidunt ut labore et dolore magna aliquyam</p>
  <a class="btn abs" href="#">Beratung vereinbaren</a>
  <div class="device abs" role="img" aria-label="Laptop mit Dashboard einer Software-Anwendung"></div>
</header>
<div class="hero-strip abs"></div>

<!-- Portfolio -->
<div class="portfolio-bg abs"></div>
<section class="portfolio">
  <div class="portfolio-panel abs"></div>
  <div class="eyebrow abs sec-head" style="top:616px">Portfolio</div>
  <h2 class="abs sec-head" style="top:634px">Intelligente Software- und <span class="accent">Beratungslösungen</span></h2>
  <p class="portfolio-text abs">Lorem ipsum dolor sit amet, consetetur sadipscing elitr, sed diam nonumy eirmod tempor invidunt ut labore et dolore magna aliquyam erat, sed diam voluptua. At vero eos et accusam et justo duo dolores et</p>

  <article class="card abs" style="left:226px;top:751px"><div class="photo" role="img" aria-label="Foto: Person arbeitet am Tablet"></div><h3>Digitalisierung</h3><p>Lorem ipsum dolor sit amet, consetetur sadipscing elitr, sed diam nonumy eirmod tempor invidunt ut labore et dolore magna</p><a class="link" href="#">mehr erfahren</a></article>
  <article class="card abs" style="left:531px;top:751px"><div class="photo" role="img" aria-label="Foto: Team bespricht Prozesse am Laptop"></div><h3>Prozessoptimierung</h3><p>Lorem ipsum dolor sit amet, consetetur sadipscing elitr, sed diam nonumy eirmod tempor invidunt ut labore et dolore magna</p><a class="link" href="#">mehr erfahren</a></article>
  <article class="card abs" style="left:836px;top:751px"><div class="photo" role="img" aria-label="Foto: Kollegen am Bildschirm"></div><h3>Onlineanwendung</h3><p>Lorem ipsum dolor sit amet, consetetur sadipscing elitr, sed diam nonumy eirmod tempor invidunt ut labore et dolore magna</p><a class="link" href="#">mehr erfahren</a></article>
  <article class="card abs" style="left:226px;top:1156px"><div class="photo" role="img" aria-label="Foto: Apotheker in der Apotheke"></div><h3>eRezept / E-Health</h3><p>Lorem ipsum dolor sit amet, consetetur sadipscing elitr, sed diam nonumy eirmod tempor invidunt ut labore et dolore magna</p><a class="link" href="#">mehr erfahren</a></article>
  <article class="card abs" style="left:531px;top:1156px"><div class="photo" role="img" aria-label="Foto: Beratungsgespräch im Team"></div><h3>Consulting</h3><p>Lorem ipsum dolor sit amet, consetetur sadipscing elitr, sed diam nonumy eirmod tempor invidunt ut labore et dolore magna</p><a class="link" href="#">mehr erfahren</a></article>
  <article class="card abs" style="left:836px;top:1156px"><div class="photo" role="img" aria-label="Foto: Projektteam bei der Planung"></div><h3>Projektmanagement</h3><p>Lorem ipsum dolor sit amet, consetetur sadipscing elitr, sed diam nonumy eirmod tempor invidunt ut labore et dolore magna</p><a class="link" href="#">mehr erfahren</a></article>
</section>

<!-- Features -->
<section class="features">
  <div class="eyebrow abs" style="left:176px;top:1711px">Lösungen für das Gesundheitswesen</div>
  <h2 class="abs" style="left:176px;top:1730px">Mit einem erfahrenen Team und höchster <span class="accent">Fachkompetenz</span> bieten wir Lösungen, die Ihr Unternehmen im digitalen Wandel des Gesundheitswesens unterstützen.</h2>

  <div class="feature abs" style="left:176px;top:1902px">
    <svg width="46" height="52" viewBox="0 0 46 52" fill="none" stroke="#e30713" stroke-width="1.6"><path d="M16 2h14v14h14v14H30v14H16V30H2V16h14z"/><circle cx="30" cy="30" r="4"/></svg>
    <h3>Erfahrung im<br>Gesundheitswesen</h3>
    <p>Lorem ipsum dolor sit amet, consetetur sadipscing elitr, sed diam nonumy eirmod tempor invidunt ut labore et dolore magna aliquyam erat, sed diam</p>
  </div>
  <div class="feature abs" style="left:437px;top:1902px">
    <svg width="46" height="54" viewBox="0 0 46 54" fill="none" stroke="#e30713" stroke-width="1.6"><circle cx="20" cy="22" r="8"/><path d="M20 6v5M20 33v5M4 22h5M31 22h5M9 11l3.5 3.5M27.5 29.5L31 33M9 33l3.5-3.5M27.5 14.5L31 11"/><path d="M30 40v10M36 36v14"/></svg>
    <h3>Starke Fachkompetenz &amp;<br>IT-Know-How</h3>
    <p>Lorem ipsum dolor sit amet, consetetur sadipscing elitr, sed diam nonumy eirmod tempor invidunt ut labore et dolore magna aliquyam erat,</p>
  </div>
  <div class="feature abs" style="left:697px;top:1902px">
    <svg width="54" height="52" viewBox="0 0 54 52" fill="none" stroke="#e30713" stroke-width="1.6"><circle cx="27" cy="24" r="22"/><path d="M20 46V22h14v24M24 22v-8h6v8M12 46V32h8M34 36h8v10"/></svg>
    <h3>Innovative Lösungen &amp; schlanke<br>Prozesse</h3>
    <p>Lorem ipsum dolor sit amet, consetetur sadipscing elitr, sed diam nonumy eirmod tempor invidunt ut labore et dolore magna aliquyam erat, sed diam</p>
  </div>
</section>

<!-- CTA -->
<section class="cta abs">
  <h2>Gestalten Sie jetzt Ihre digitale Zukunft und sprechen Sie mit uns.</h2>
  <p>Lorem ipsum dolor sit amet, consetetur sadipscing elitr, sed diam nonumy eirmod tempor invidunt ut labore et dolore magna aliquyam erat, sed diam</p>
  <a class="btn" href="#">Beratung vereinbaren</a>
</section>

<!-- About & Jobs -->
<div class="lower-bg abs"></div>
<div class="panel abs" style="left:217px;top:2716px;width:894px;height:377px"></div>
<div class="photo-block abs" style="left:88px;top:2778px;width:417px;height:437px" role="img" aria-label="Foto: zwei Kollegen mit Laptop im Büro"></div>
<div class="text-block abs" style="left:598px;top:2796px;width:430px">
  <div class="eyebrow">Über uns</div>
  <h2 style="margin-top:14px">Mit unserem Know-how und der jahrelangen <span class="accent">Markterfahrung</span> bieten wir flexible Lösungen</h2>
  <p>Lorem ipsum dolor sit amet, consetetur sadipscing elitr, sed diam nonumy eirmod tempor invidunt ut labore et dolore magna aliquyam erat, sed diam voluptua. At vero eos et</p>
  <a class="link" href="#">mehr über uns erfahren</a>
</div>

<div class="panel abs" style="left:88px;top:3254px;width:896px;height:376px"></div>
<div class="photo-block abs" style="left:694px;top:3315px;width:417px;height:440px;background:linear-gradient(150deg,#c9b37a,#5d6470)" role="img" aria-label="Foto: Kollegen arbeiten gemeinsam am Laptop"></div>
<div class="text-block abs" style="left:176px;top:3358px;width:380px">
  <div class="eyebrow">Arbeiten bei VMT</div>
  <h2 style="margin-top:14px">Wir stehen für kompetente Zusammenarbeit auf Augenhöhe</h2>
  <p>Lorem ipsum dolor sit amet, consetetur sadipscing elitr, sed diam nonumy eirmod tempor invidunt ut labore et dolore magna aliquyam erat, sed diam voluptua. At vero eos et</p>
  <a class="link" href="#">Stellenangebote anschauen</a>
</div>

<!-- Partners -->
<section class="partners abs">
  <div class="eyebrow">Kunden</div>
  <h2>Unsere zufriedenen Partner</h2>
</section>
<div class="partner abs" style="left:174px"></div>
<div class="partner abs" style="left:358px"></div>
<div class="partner abs" style="left:542px"></div>
<div class="partner abs" style="left:726px"></div>
<div class="partner abs" style="left:909px"></div>

<!-- Footer -->
<footer class="footer abs">
  <div class="abs" style="left:88px;top:46px">
    <div class="brand">VMT</div>
    <div class="brand-sub">SOFTWARE FÜR DAS GESUNDHEITSWESEN</div>
  </div>
  <div class="f-col" style="left:290px">
    <h4>Kontakt</h4>
    <div class="f-row"><svg width="14" height="14" viewBox="0 0 24 24" fill="#f07a45"><path d="M6.6 10.8a15.1 15.1 0 006.6 6.6l2.2-2.2a1 1 0 011-.25 11.4 11.4 0 003.6.57 1 1 0 011 1V20a1 1 0 01-1 1A17 17 0 013 4a1 1 0 011-1h3.5a1 1 0 011 1c0 1.25.2 2.45.57 3.57a1 1 0 01-.25 1z"/></svg>+49 21 40 / 5 20 18 - 00</div>
    <div class="f-row"><svg width="14" height="14" viewBox="0 0 24 24" fill="#f07a45"><path d="M2 5h20v14H2z"/><path d="M2 5l10 8 10-8" stroke="#1e264a" stroke-width="2" fill="none"/></svg>info@vmt-pflegeloesung.de</div>
    <div class="f-row"><svg width="14" height="14" viewBox="0 0 24 24" fill="none" stroke="#f07a45" stroke-width="2"><circle cx="12" cy="12" r="10"/><path d="M2 12h20M12 2c3 3 3 17 0 20M12 2c-3 3-3 17 0 20"/></svg>vmt-pflegeloesung.de</div>
    <div class="f-row"><svg width="14" height="16" viewBox="0 0 24 28" fill="#f07a45"><path d="M12 0a9 9 0 019 9c0 7-9 19-9 19S3 16 3 9a9 9 0 019-9z"/><circle cx="12" cy="9" r="3.5" fill="#1e264a"/></svg><span>VMT AG<br>Lindenweg 14<br>40210 Musterstadt</span></div>
  </div>
  <div class="f-col" style="left:662px">
    <h4>Leistungen</h4>
    <ul class="f-list"><li>Prozessoptimierung</li><li>Digitalisierung</li><li>Onlineanwendung</li><li>eRezept / E-Health</li><li>Consulting</li><li>Projektmanagement</li></ul>
  </div>
  <div class="f-col" style="left:870px">
    <h4>Unternehmen</h4>
    <ul class="f-list"><li>Produkte</li><li>Über Uns</li><li>Jobangebote</li><li>Kontakt</li></ul>
  </div>
  <div class="f-bottom">
    <span>© &nbsp;VMT - Softwareentwicklung für das Gesundheitswesen</span>
    <span class="legal"><span>Impressum</span><span>Datenschutz</span><span>Cookie-Einstellungen</span></span>
  </div>
</footer>

</body>
</html>
```